Child Care Web Page

We need a web page for a child care center, children ages 6 weeks to prekindergarten. We are licensed by the state of Colorado, accredited by the Federated Council for Early Learning Standards Board. The design should be colorful, parent and user friendly.
Updates

Project Deadline Extended
Reason: Difficulty of project

Target Market(s)

Parents, staff, general community, early childhood professionals

Industry/Entity Type

Education

Requirements
Must have
• I would like to have designers that are willing to work with me in developing a site that I am able to make changes to and help with the learning curve.

```html
<!DOCTYPE html>
<html lang="en">
<head>
<meta charset="utf-8">
<title>Child Care Center</title>
<link rel="stylesheet" href="https://fonts.googleapis.com/css2?family=Open+Sans:wght@400;600&family=PT+Sans:wght@400;700&display=swap">
<style>
:root{
  --plum:#660066;
  --plum-deep:#330033;
  --plum-footer:#5a0f55;
  --heading:#4a0a48;
  --brown:#341e17;
  --orange:#f39c1e;
  --body-text:#5a5a5a;
  --white:#ffffff;
}
*{box-sizing:border-box;margin:0;padding:0}
html,body{width:823px;height:1200px;overflow:hidden;background:var(--white)}
body{position:relative;font-family:"PT Sans",sans-serif}
.topbar{position:absolute;left:0;top:0;width:823px;height:78px;background:var(--plum)}
.account-links{position:absolute;right:40px;top:54px;font-size:11px;color:var(--orange)}
.account-links a{color:var(--orange);text-decoration:none}
.account-links span{margin:0 5px}
.hero{position:absolute;left:0;top:78px;width:823px;height:387px;
  background:linear-gradient(90deg,#8a5a7a 0%,#c9a3b4 25%,#e8cfc8 50%,#f3e6e2 75%,#f7efee 100%)}
.hero-title{position:absolute;left:34px;top:140px;font-family:"Open Sans",sans-serif;font-weight:600;
  font-size:49px;line-height:53px;color:var(--white);text-shadow:2px 3px 4px rgba(0,0,0,.55)}
.hero-btn{position:absolute;top:326px;width:243px;height:32px;background:var(--brown);color:var(--white);
  font-size:13px;line-height:32px;text-align:center;text-decoration:none}
.hero-btn.providers{left:159px}
.hero-btn.families{left:411px}
.hero-band{position:absolute;left:0;top:465px;width:823px;height:15px;background:var(--plum-deep)}
.main-nav{position:absolute;top:494px;left:156px;display:flex;gap:5px}
.main-nav a{display:block;width:166px;height:26px;background:var(--plum);color:var(--white);
  font-size:13px;line-height:26px;text-align:center;text-decoration:none}
.content{position:absolute;left:48px;width:434px}
.content h2{font-weight:400;font-size:27px;line-height:34px;color:var(--heading);margin-bottom:10px}
.content p{font-size:12px;line-height:15.5px;color:var(--body-text);text-align:justify}
.c1{top:576px}.c2{top:700px}.c3{top:823px}
.callbox{position:absolute;left:536px;top:589px;width:248px;height:170px;background:var(--brown);
  color:var(--white);text-align:center;padding-top:34px}
.callbox .label{font-size:28px;line-height:32px}
.callbox .number{font-size:29px;line-height:34px}
.callbox .tty{font-size:15px;line-height:18px;font-weight:700}
.searchbox{position:absolute;left:537px;top:807px;width:248px;height:170px;background:var(--brown);color:var(--white)}
.searchbox h3{position:absolute;left:28px;top:24px;width:210px;font-weight:400;font-size:27px;line-height:34px;text-align:center}
.searchbox .field{position:absolute;left:28px;top:111px;width:154px;height:23px;background:#cdbfbc;border:0}
.searchbox .go{position:absolute;left:186px;top:111px;width:31px;height:23px;background:#cdbfbc;color:var(--brown);
  font-size:14px;font-weight:700;line-height:23px;text-align:center;border:0}
.footer{position:absolute;left:0;top:1027px;width:823px;height:173px;background:var(--plum-footer)}
.footer-col{position:absolute;top:24px;width:170px}
.footer-col h4{font-weight:400;font-size:16px;color:var(--orange);text-align:center;margin-bottom:6px}
.footer-col p{font-size:10.5px;line-height:13px;color:#e6d0e2}
.footer-col a{display:block;margin-top:12px;font-size:10px;font-style:italic;color:var(--orange);text-decoration:none}
.divider{position:absolute;left:60px;top:132px;width:703px;height:1px;background:rgba(255,255,255,.12)}
.copyright{position:absolute;top:144px;width:100%;text-align:center;font-size:11px;color:#e6d0e2}
</style>
</head>
<body>
<header class="topbar">
  <nav class="account-links"><a href="#">Register</a><span>|</span><a href="#">Login</a></nav>
</header>
<section class="hero" role="img" aria-label="Photograph of a baby sitting beside a young family playing together on the floor">
  <h1 class="hero-title">Child Care<br>Center</h1>
  <a class="hero-btn providers" href="#">Child Care Providers</a>
  <a class="hero-btn families" href="#">Parents and Familes</a>
</section>
<div class="hero-band"></div>
<nav class="main-nav"><a href="#">About Us</a><a href="#">Help</a><a href="#">Contact Us</a></nav>

<section class="content c1">
  <h2>Child Care Center?</h2>
  <p>As a Brightway Gold partner, we have over 19 years experience of delivering successful Business Intelligence, Performance Management, Custom Development and Business Process solutions.</p>
</section>
<section class="content c2">
  <h2>Are you Aware?</h2>
  <p>As a Brightway Gold partner, we have over 19 years experience of delivering successful Business Intelligence, Performance Management, Custom Development and Business Process solutions.</p>
</section>
<section class="content c3">
  <h2>Little Steps Alliance of Americas Cost?</h2>
  <p>As a Brightway Gold partner, we have over 19 years experience of delivering successful Business Intelligence, Performance Management, Custom Development and Business Process solutions.</p>
</section>

<aside class="callbox">
  <div class="label">Call Toll Free:</div>
  <div class="number">1-800-555-0142</div>
  <div class="tty">Call TTY#: 1-866-555-0187</div>
</aside>
<aside class="searchbox">
  <h3>Free Child Care Search</h3>
  <div class="field"></div>
  <div class="go">Go</div>
</aside>

<footer class="footer">
  <div class="footer-col" style="left:60px"><h4>News</h4><p>Dummy text dummy text dummy text dummy text Dummy text</p><a href="#">Learn more...</a></div>
  <div class="footer-col" style="left:249px"><h4>Updates</h4><p>Dummy text dummy text dummy text dummy text Dummy text</p><a href="#">Learn more...</a></div>
  <div class="footer-col" style="left:446px"><h4>Free Check Up</h4><p>Dummy text dummy text dummy text dummy text Dummy text</p><a href="#">Learn more...</a></div>
  <div class="footer-col" style="left:633px"><h4>Downloads</h4><p>Dummy text dummy text dummy text dummy text Dummy text</p><a href="#">Learn more...</a></div>
  <div class="divider"></div>
  <p class="copyright">Copyright (c) 2013 Child Care Center. All rights reserved.</p>
</footer>
</body>
</html>
```